Zanquorra Business Card Design

Zanquorra is a small and new restaurant/ bar location in Hong Kong. The name "Djibouti" derives from an African country. There is no specific reason behind other than the fact, that the bar is somewhat inspired by African elements (only inspired but not purely based on African cuisine etc.).

The bar is somewhat a fusion of African, Mediterranean and Oriental (Old French Vietnam) elements.

However, it is very imperative to stress, that the overall look and feel of Zanquorra is a very high end cocktail lounge/ bar location. The bar is tucked away in a hidden alley, so people will have to know about it. The idea is to send the consumer off in an Escape or hidden remote location where they are at ease in a hip, stylish and trendy environment.

The card needs to feel high-end.

Final logo artwork has been attached and also pictures of the bar/ restaurant itself. The logo ie monkey head cannot be modified. However, the background color and the color of the type "ZANQUORRA" can be changed.

The following details need to fit onto the business card. Of course they can be arranged to your liking:

LOGO

Colin Vey
Partner

+852 97035164
xxx@zanquorra.com
www.zanquorra.com
7C, Brennick Road, Wan Chai, Hong Kong

```html
<!DOCTYPE html>
<html lang="en">
<head>
<meta charset="utf-8">
<title>Zanquorra Business Card</title>
<link rel="stylesheet" href="https://fonts.googleapis.com/css2?family=Old+Standard+TT:wght@400;700&display=swap">
<style>
  :root {
    --stage: #e9e4dc;
    --card: #ffffff;
    --ink: #2a211c;
    --accent: #1f72b8;
    --mark: #2b211c;
    --ring: #ffffff;
  }
  * { box-sizing: border-box; margin: 0; padding: 0; }
  html, body {
    width: 1200px; height: 900px; overflow: hidden;
    background: var(--stage);
  }
  .stage {
    position: relative; width: 1200px; height: 900px;
    display: flex; align-items: center; justify-content: center; gap: 50px;
    font-family: "Old Standard TT", Georgia, serif;
    color: var(--ink);
  }
  .card {
    position: relative; width: 525px; height: 300px;
    background: var(--card); border-radius: 18px; overflow: hidden;
    box-shadow: 0 6px 18px rgba(0,0,0,.18);
  }
  /* front */
  .front .brand-circle {
    position: absolute; right: -70px; top: -20px;
    width: 330px; height: 330px; border-radius: 50%;
    background: var(--mark);
    border: 4px solid var(--ring);
    outline: 3px solid var(--mark);
  }
  .front .brand-name {
    position: absolute; right: 30px; bottom: 18px;
    font-size: 16px; letter-spacing: 3px; color: var(--ink);
  }
  .contact { position: absolute; left: 40px; top: 52px; }
  .contact .name {
    font-size: 24px; font-weight: 700; color: var(--accent);
    letter-spacing: .5px; line-height: 1.1;
  }
  .contact .role { font-size: 17px; margin-bottom: 26px; }
  .contact .address { font-size: 16px; line-height: 1.3; margin-left: 40px; margin-bottom: 16px; }
  .contact ul { list-style: none; }
  .contact li {
    display: flex; align-items: center; gap: 10px;
    font-size: 16px; line-height: 1.45;
  }
  .contact li svg { width: 15px; height: 15px; flex: none; }
  /* back */
  .back { display: flex; flex-direction: column; align-items: center; justify-content: center; gap: 22px; }
  .back .brand-circle {
    width: 150px; height: 150px; border-radius: 50%;
    background: var(--mark);
    border: 3px solid var(--ring);
    outline: 2px solid var(--mark);
  }
  .back .brand-name {
    font-size: 40px; letter-spacing: 4px; color: var(--ink); line-height: 1;
  }
</style>
</head>
<body>
<main class="stage">
  <section class="card front">
    <div class="brand-circle" aria-hidden="true"></div>
    <div class="brand-name">ZANQUORRA</div>
    <div class="contact">
      <p class="name">COLIN VEY</p>
      <p class="role">Partner</p>
      <p class="address">7C, Brennick Road,<br>Wan Chai,<br>Hong Kong</p>
      <ul>
        <li>
          <svg viewBox="0 0 16 16"><circle cx="8" cy="8" r="8" fill="var(--accent)"/><path d="M5 4.5h2l.8 2-1.2.8a5 5 0 0 0 2.1 2.1l.8-1.2 2 .8v2a1 1 0 0 1-1 1A7 7 0 0 1 4 5.5a1 1 0 0 1 1-1z" fill="#fff"/></svg>
          +852 97035164
        </li>
        <li>
          <svg viewBox="0 0 16 16"><circle cx="8" cy="8" r="8" fill="var(--accent)"/><rect x="4" y="5" width="8" height="6" fill="#fff"/><path d="M4 5l4 3.5L12 5" fill="none" stroke="var(--accent)" stroke-width="1"/></svg>
          xxx@zanquorra.com
        </li>
        <li>
          <svg viewBox="0 0 16 16"><circle cx="8" cy="8" r="8" fill="var(--accent)"/><g fill="none" stroke="#fff" stroke-width="1"><circle cx="8" cy="8" r="4.5"/><ellipse cx="8" cy="8" rx="2" ry="4.5"/><path d="M3.5 8h9"/></g></svg>
          www.zanquorra.com
        </li>
      </ul>
    </div>
  </section>

  <section class="card back">
    <div class="brand-circle" aria-hidden="true"></div>
    <div class="brand-name">ZANQUORRA</div>
  </section>
</main>
</body>
</html>
```